Business Cards for, Telori Basuvenka - Spending Planner, employed by Clear Path Spending Planner - new business based in Brisbane Australia.

Small Business providing 'Spending Planing' services. Helping people, families, homes, businesses achieve their budgeting goals.

Motto: Counting Wisely Grows Futures

Final design should communicate financial freedom and strong positive growth.

Target Market(s)

Working Families, Finance, Retail,

Industry/Entity Type

Finance

Contact Information for Business Card

Name, Company Title
Mobile details, Email details

Logo Text

Clear Path Spending Planner - Counting Wisely Grows Futures

Font styles to use
Serif

Requirements
Must have
• Easy to read
Nice to have
• Modern Looking
Should not have
• Not too confusing to understand

```html
<!DOCTYPE html>
<html lang="en">
<head>
<meta charset="UTF-8">
<title>Clear Path Spending Planner – Stationery</title>
<link href="https://fonts.googleapis.com/css2?family=Libre+Caslon+Text:wght@400;700&family=Open+Sans:ital,wght@0,400;0,600;1,400;1,600&display=swap" rel="stylesheet">
<style>
  :root {
    --brand-blue: #1d5ea8;
    --card-blue: #1a5fa7;
    --steel: #8e9aa7;
    --ink: #3b3f45;
    --muted: #7a8089;
    --paper: #ffffff;
    --stage: #eceef1;
    --hairline: #d7dbe0;
  }
  * { box-sizing: border-box; margin: 0; padding: 0; }
  html, body { width: 1200px; height: 2250px; overflow: hidden; }
  body { background: var(--paper); font-family: "Open Sans", Arial, sans-serif; color: var(--ink); }

  .brand-wordmark { font-family: "Libre Caslon Text", Georgia, serif; color: var(--brand-blue); font-weight: 400; text-transform: uppercase; white-space: nowrap; }
  .brand-tagline { font-family: "Libre Caslon Text", Georgia, serif; text-transform: uppercase; white-space: nowrap; }
  .brand-square { background: var(--brand-blue); flex: none; }

  /* Lockup */
  .identity { height: 470px; display: flex; align-items: center; justify-content: center; gap: 44px; }
  .identity .brand-square { width: 120px; height: 120px; }
  .identity .divider { width: 2px; height: 150px; background: var(--steel); }
  .identity .brand-wordmark { font-size: 44px; line-height: 1; letter-spacing: 0.5px; }
  .identity .brand-tagline { font-size: 15px; letter-spacing: 8px; color: #555; margin-top: 14px; text-align: center; }

  /* Cards */
  .cards { height: 860px; background: var(--stage); display: flex; align-items: center; justify-content: center; gap: 60px; }
  .card { width: 480px; height: 274px; position: relative; overflow: hidden; box-shadow: 0 14px 30px rgba(0,0,0,0.12); }
  .card-front { background: var(--paper); }
  .card-front .brand-square { position: absolute; left: 40px; top: 34px; width: 38px; height: 38px; }
  .card-front .holder { position: absolute; left: 40px; top: 92px; }
  .holder-name { font-size: 21px; font-weight: 600; font-style: italic; color: var(--brand-blue); }
  .holder-title { font-size: 12px; font-style: italic; color: var(--muted); margin-top: 2px; }
  .contact-list { position: absolute; right: 34px; bottom: 50px; list-style: none; font-size: 12px; color: var(--ink); }
  .contact-list li { display: flex; align-items: flex-start; gap: 9px; margin-top: 6px; line-height: 1.35; }
  .contact-list svg { width: 12px; height: 12px; flex: none; margin-top: 2px; fill: var(--brand-blue); }
  .edge-stripe { position: absolute; left: 0; right: 0; bottom: 16px; height: 5px; display: flex; align-items: flex-end; }
  .edge-stripe .blue { width: 58%; height: 5px; background: var(--brand-blue); }
  .edge-stripe .grey { flex: 1; height: 2px; background: var(--steel); }

  .card-back { background: var(--card-blue); display: flex; flex-direction: column; align-items: center; justify-content: center; }
  .card-back .brand-square { width: 50px; height: 50px; background: var(--paper); margin-bottom: 22px; }
  .card-back .brand-wordmark { color: var(--paper); font-size: 22px; }
  .card-back .brand-tagline { color: #dce7f4; font-size: 8px; letter-spacing: 4.5px; margin-top: 7px; }

  /* Letterhead */
  .letter-set { height: 920px; background: var(--stage); position: relative; }
  .letterhead { position: absolute; left: 140px; top: 50px; width: 600px; height: 820px; background: var(--paper); box-shadow: 0 14px 30px rgba(0,0,0,0.12); padding: 48px 52px; font-size: 10.5px; line-height: 1.6; overflow: hidden; }
  .letterhead-top { display: flex; justify-content: space-between; align-items: flex-start; }
  .mini-lockup { display: flex; align-items: center; gap: 12px; }
  .mini-lockup .brand-square { width: 22px; height: 22px; }
  .mini-lockup .divider { width: 1px; height: 28px; background: var(--steel); }
  .mini-lockup .brand-wordmark { font-size: 12px; }
  .mini-lockup .brand-tagline { font-size: 5.5px; letter-spacing: 2.5px; color: #666; margin-top: 3px; }
  .letterhead .contact-list { position: static; font-size: 8.5px; }
  .letterhead .contact-list li { margin-top: 2px; gap: 6px; }
  .letterhead .contact-list svg { width: 8px; height: 8px; }
  .recipient { margin-top: 60px; }
  .letter-body p { margin-top: 14px; }
  .letter-body { margin-top: 18px; }
  .sign-off { margin-top: 26px; }
  .signature { width: 120px; height: 44px; margin: 8px 0 4px; background: linear-gradient(90deg, #e9ecef, #f5f6f8); }
  .signer { font-size: 9.5px; color: var(--muted); }
  .letterhead .edge-stripe { bottom: 26px; }

  .small-cards { position: absolute; right: 110px; top: 290px; display: flex; flex-direction: column; gap: 40px; }
  .small-cards .card { width: 320px; height: 183px; }
  .small-cards .card-front .brand-square { left: 26px; top: 24px; width: 26px; height: 26px; }
  .small-cards .card-front .holder { left: 26px; top: 62px; }
  .small-cards .holder-name { font-size: 14px; }
  .small-cards .holder-title { font-size: 8.5px; }
  .small-cards .contact-list { right: 22px; bottom: 32px; font-size: 8px; }
  .small-cards .contact-list li { margin-top: 3px; gap: 6px; }
  .small-cards .contact-list svg { width: 8px; height: 8px; }
  .small-cards .edge-stripe { bottom: 11px; }
  .small-cards .card-back .brand-square { width: 34px; height: 34px; margin-bottom: 14px; }
  .small-cards .card-back .brand-wordmark { font-size: 14.5px; }
  .small-cards .card-back .brand-tagline { font-size: 5.5px; letter-spacing: 3px; margin-top: 5px; }
</style>
</head>
<body>

<svg width="0" height="0" style="position:absolute">
  <symbol id="icon-pin" viewBox="0 0 12 12"><path d="M6 0a4.2 4.2 0 0 0-4.2 4.2C1.8 7.3 6 12 6 12s4.2-4.7 4.2-7.8A4.2 4.2 0 0 0 6 0zm0 5.8a1.6 1.6 0 1 1 0-3.2 1.6 1.6 0 0 1 0 3.2z"/></symbol>
  <symbol id="icon-phone" viewBox="0 0 12 12"><path d="M2.4 0.6l2 2.2-1 1.4c.7 1.6 2 2.9 3.5 3.6l1.4-1 2.2 2-1.2 2.2C4.8 10.7 1.3 7.2.6 2.7z"/></symbol>
  <symbol id="icon-mail" viewBox="0 0 12 12"><path d="M0 2h12v8H0zm1.2 1.2v.3L6 6.6l4.8-3.1v-.3zM1.2 5v3.8h9.6V5L6 8.1z"/></symbol>
  <symbol id="icon-globe" viewBox="0 0 12 12"><path d="M6 0a6 6 0 1 0 0 12A6 6 0 0 0 6 0zm4.6 5.3H8.7a9 9 0 0 0-.9-3.9 4.7 4.7 0 0 1 2.8 3.9zM6 1.3c.7.9 1.2 2.4 1.3 4H4.7c.1-1.6.6-3.1 1.3-4zM4.2 1.4a9 9 0 0 0-.9 3.9H1.4a4.7 4.7 0 0 1 2.8-3.9zM1.4 6.7h1.9c.1 1.5.4 2.8.9 3.9a4.7 4.7 0 0 1-2.8-3.9zM6 10.7c-.7-.9-1.2-2.4-1.3-4h2.6c-.1 1.6-.6 3.1-1.3 4zm1.8-.1c.5-1.1.8-2.4.9-3.9h1.9a4.7 4.7 0 0 1-2.8 3.9z"/></symbol>
</svg>

<header class="identity">
  <div class="brand-square"></div>
  <div class="divider"></div>
  <div>
    <div class="brand-wordmark">Clear Path Spending Planner</div>
    <div class="brand-tagline">Counting Wisely Grows Futures</div>
  </div>
</header>

<section class="cards">
  <article class="card card-front">
    <div class="brand-square"></div>
    <div class="holder">
      <div class="holder-name">Telori Basuvenka</div>
      <div class="holder-title">Spending Planner</div>
    </div>
    <ul class="contact-list">
      <li><svg><use href="#icon-pin"/></svg><span>48 Wattle Lane<br>Brisbane QLD 4101</span></li>
      <li><svg><use href="#icon-phone"/></svg><span>07 3184 2650</span></li>
      <li><svg><use href="#icon-mail"/></svg><span>hello@clearpathplanner.au</span></li>
      <li><svg><use href="#icon-globe"/></svg><span>www.clearpathplanner.au</span></li>
    </ul>
    <div class="edge-stripe"><span class="blue"></span><span class="grey"></span></div>
  </article>
  <article class="card card-back">
    <div class="brand-square"></div>
    <div class="brand-wordmark">Clear Path Spending Planner</div>
    <div class="brand-tagline">Counting Wisely Grows Futures</div>
  </article>
</section>

<section class="letter-set">
  <article class="letterhead">
    <div class="letterhead-top">
      <div class="mini-lockup">
        <div class="brand-square"></div>
        <div class="divider"></div>
        <div>
          <div class="brand-wordmark">Clear Path Spending Planner</div>
          <div class="brand-tagline">Counting Wisely Grows Futures</div>
        </div>
      </div>
      <ul class="contact-list">
        <li><svg><use href="#icon-phone"/></svg><span>07 3184 2650</span></li>
        <li><svg><use href="#icon-mail"/></svg><span>hello@clearpathplanner.au</span></li>
        <li><svg><use href="#icon-globe"/></svg><span>www.clearpathplanner.au</span></li>
      </ul>
    </div>
    <address class="recipient" style="font-style:normal">
      To,<br>Mr. Arlen Moss<br>Chief Operating Officer<br>Harbourline Goods<br>48 Quay Road<br>Brisbane QLD 4000
    </address>
    <div class="letter-body">
      <p>Thank you for meeting with us last week to talk about your household and business budgets. We have reviewed your spending records and prepared a simple plan that sets clear monthly targets, builds a steady savings buffer and trims costs that no longer serve your goals.</p>
      <p>Each step is easy to follow, and we will check in every month to track progress and adjust the plan as your needs change.</p>
      <p>Please reach out with any questions before our next session. We look forward to helping you grow with confidence.</p>
    </div>
    <div class="sign-off">Yours faithfully,</div>
    <div class="signature" role="img" aria-label="Handwritten signature"></div>
    <div class="signer">Telori Basuvenka</div>
    <div class="edge-stripe"><span class="blue"></span><span class="grey"></span></div>
  </article>

  <div class="small-cards">
    <article class="card card-front">
      <div class="brand-square"></div>
      <div class="holder">
        <div class="holder-name">Telori Basuvenka</div>
        <div class="holder-title">Spending Planner</div>
      </div>
      <ul class="contact-list">
        <li><svg><use href="#icon-pin"/></svg><span>48 Wattle Lane<br>Brisbane QLD 4101</span></li>
        <li><svg><use href="#icon-phone"/></svg><span>07 3184 2650</span></li>
        <li><svg><use href="#icon-mail"/></svg><span>hello@clearpathplanner.au</span></li>
        <li><svg><use href="#icon-globe"/></svg><span>www.clearpathplanner.au</span></li>
      </ul>
      <div class="edge-stripe"><span class="blue"></span><span class="grey"></span></div>
    </article>
    <article class="card card-back">
      <div class="brand-square"></div>
      <div class="brand-wordmark">Clear Path Spending Planner</div>
      <div class="brand-tagline">Counting Wisely Grows Futures</div>
    </article>
  </div>
</section>

</body>
</html>
```